Tidal Pines - explore habits of productive people

Tidal Pines is a social place around habits and productivity

The full brief below:

https://docs.quorvane.net/document/d/7Rt-PWMZXK4ubEhqNcs-V2Ytm9Gx8KdfHzJqBsQwnyrT/edit?usp=sharing

Colors

Designer to choose colors to be used in the design.

Requirements
Must have
• - a feed page to display habits
• - a habit page to add a habit
• / clean, no cluttered design, lots of white space
• / inspired by lattice design or other design system
Nice to have
• - user page

```html
<!DOCTYPE html>
<html lang="en">
<head>
<meta charset="utf-8">
<title>Tidal Pines – Discover</title>
<link href="https://fonts.googleapis.com/css2?family=Poppins:wght@400;500;600&display=swap" rel="stylesheet">
<style>
  :root{
    --page:#fff6f3;
    --surface:#ffffff;
    --canvas:#f4f4f4;
    --line:#ececec;
    --ink:#3c3c3c;
    --ink-soft:#8d8d8d;
    --ink-mute:#9a9a9a;
    --accent:#ff8a5b;
    --accent-tint:#ffeee7;
    --good:#2bc47e;
    --good-tint:#dcf6e9;
    --bad:#ef5f58;
    --bad-tint:#ffe2de;
    --heart:#f25656;
    --chip:#ededed;
    --chip-ink:#9a9a9a;
  }
  *{box-sizing:border-box;margin:0;padding:0}
  html,body{width:1200px;height:1200px;overflow:hidden;background:var(--page);font-family:"Poppins",sans-serif;color:var(--ink)}
  .app{position:absolute;left:24px;top:240px;width:1152px;height:720px;background:var(--surface);overflow:hidden}
  .topbar{height:72px;border-bottom:1px solid var(--line);display:flex;align-items:center;justify-content:space-between;padding:0 32px 0 31px}
  .brand{font-size:21px;font-weight:500;letter-spacing:.5px;color:var(--ink)}
  .topbar-actions{display:flex;align-items:center;gap:26px}
  .bell{position:relative;width:26px;height:28px}
  .bell-dot{position:absolute;right:2px;top:2px;width:6px;height:6px;border-radius:50%;background:var(--accent)}
  .avatar-lg{width:40px;height:40px;border-radius:50%;background:linear-gradient(135deg,#2a3140,#141821)}
  .body{display:flex;height:648px}
  .sidebar{width:215px;background:var(--surface);padding-top:38px;flex-shrink:0}
  .add-btn{margin-left:39px;width:138px;height:40px;background:var(--accent);color:#fff;border:none;font:500 15px "Poppins",sans-serif;display:flex;align-items:center;justify-content:center;gap:8px;box-shadow:0 6px 14px rgba(255,138,91,.3);border-radius:2px}
  .nav{list-style:none;margin-top:43px}
  .nav-item{height:54px;display:flex;align-items:center;gap:17px;padding-left:33px;font-size:14.5px;color:var(--ink-mute)}
  .nav-item svg{width:20px;height:20px;fill:#a3a3a3}
  .nav-item.is-active{background:var(--accent-tint);color:var(--accent);border-left:3px solid var(--accent);padding-left:30px}
  .nav-item.is-active svg{fill:var(--accent)}
  .main{flex:1;background:var(--canvas);padding:30px 40px 0 40px;overflow:hidden}
  .filter-bar{height:80px;background:var(--surface);border:1px solid var(--line);border-radius:3px;display:flex;align-items:center;padding-left:38px}
  .filter-label{font-size:14.5px;font-weight:500;margin-right:30px}
  .chip{height:24px;padding:0 11px;margin-right:20px;background:var(--chip);color:var(--chip-ink);font-size:11.5px;font-weight:500;display:flex;align-items:center;letter-spacing:.3px;border-radius:2px}
  .chip.is-active{background:var(--accent-tint);color:var(--accent)}
  .feed{display:flex;gap:16px;margin-top:20px;align-items:flex-start}
  .feed-col{width:420px;display:flex;flex-direction:column;gap:20px}
  .feed-col.offset{margin-top:-1px}
  .card{background:var(--surface);border-radius:3px;padding:20px 20px 24px;position:relative}
  .tag{display:inline-block;font-size:11.5px;font-weight:500;padding:3px 8px;border-radius:2px}
  .tag.good{background:var(--good-tint);color:var(--good)}
  .tag.bad{background:var(--bad-tint);color:var(--bad)}
  .like{position:absolute;right:21px;top:22px;width:20px;height:20px}
  .section-label{color:var(--accent);font-size:14.5px;font-weight:500;margin-top:14px}
  .habit-title{font-size:14.5px;font-weight:500;margin-top:7px}
  .loop-step{font-size:12.8px;line-height:19.2px;color:var(--ink-soft);margin-top:15px}
  .loop-step:first-of-type{margin-top:6px}
  .loop-step b{color:var(--ink);font-weight:600}
  .contribute{display:flex;justify-content:flex-end;align-items:center;gap:7px;color:var(--accent);font-weight:600;font-size:14.5px;margin-top:20px}
  .contribute svg{width:15px;height:15px;fill:var(--accent)}
  .author{display:flex;align-items:center;gap:10px;margin-top:12px;font-size:14.5px;font-weight:500}
  .avatar-sm{width:24px;height:24px;border-radius:50%}
  .placeholder{height:40px}
</style>
</head>
<body>
<div class="app">
  <header class="topbar">
    <div class="brand">TIDAL PINES</div>
    <div class="topbar-actions">
      <div class="bell">
        <svg viewBox="0 0 24 26" width="26" height="28"><path d="M12 1a2 2 0 0 1 2 2v1.2c3.4.9 5.5 3.8 5.5 7.3v5.5l2.5 3v1H2v-1l2.5-3v-5.5c0-3.5 2.1-6.4 5.5-7.3V3a2 2 0 0 1 2-2zm-3 22h6a3 3 0 0 1-6 0z" fill="#a3a3a3"/></svg>
        <span class="bell-dot"></span>
      </div>
      <div class="avatar-lg" role="img" aria-label="Profile photo of the signed-in user"></div>
    </div>
  </header>
  <div class="body">
    <aside class="sidebar">
      <button class="add-btn"><svg width="14" height="14" viewBox="0 0 14 14"><path d="M7 1v12M1 7h12" stroke="#fff" stroke-width="2" stroke-linecap="round"/></svg>Add Habit</button>
      <ul class="nav">
        <li class="nav-item is-active"><svg viewBox="0 0 20 20"><circle cx="10" cy="10" r="9"/><path d="M13.5 6.5 11.2 11.2 6.5 13.5 8.8 8.8z" fill="#fff"/></svg>Discover</li>
        <li class="nav-item"><svg viewBox="0 0 20 20"><path d="M3 2h14v16H3z"/><path d="M11 2h4v7l-2-1.5L11 9z" fill="#fff"/></svg>Your Habits</li>
        <li class="nav-item"><svg viewBox="0 0 20 20"><path d="M10 18 2.6 10.6A4.6 4.6 0 0 1 10 4.4a4.6 4.6 0 0 1 7.4 6.2z"/></svg>Adopted Habits</li>
        <li class="nav-item"><svg viewBox="0 0 20 20"><path d="M8.6 1h2.8l.5 2.5 1.7.8 2.2-1.4 2 2-1.4 2.2.8 1.7 2.5.5v2.8l-2.5.5-.8 1.7 1.4 2.2-2 2-2.2-1.4-1.7.8-.5 2.5H8.6l-.5-2.5-1.7-.8-2.2 1.4-2-2 1.4-2.2-.8-1.7L.3 11.4V8.6l2.5-.5.8-1.7-1.4-2.2 2-2 2.2 1.4 1.7-.8zM10 7a3 3 0 1 0 0 6 3 3 0 0 0 0-6z"/></svg>Settings</li>
      </ul>
    </aside>
    <main class="main">
      <div class="filter-bar">
        <span class="filter-label">Filter:</span>
        <span class="chip">Good Habits</span>
        <span class="chip">Bad Habits</span>
        <span class="chip is-active">Newest First</span>
        <span class="chip">Most Adopted</span>
        <span class="chip">Alphabetical</span>
      </div>
      <div class="feed">
        <div class="feed-col">
          <article class="card">
            <span class="tag good">Good</span>
            <svg class="like" viewBox="0 0 20 20"><path d="M10 18 2.6 10.6A4.6 4.6 0 0 1 10 4.4a4.6 4.6 0 0 1 7.4 6.2z" fill="var(--heart)"/></svg>
            <p class="section-label">Habit</p>
            <h2 class="habit-title">Workout Every Morning Before Work</h2>
            <p class="section-label">Loop</p>
            <p class="loop-step"><b>Cue:</b> Put your gym clothes where they are clearly visible in your closet.</p>
            <p class="loop-step"><b>Craving:</b> Follow a simple workout routine that’s fun and efficient that fits within your schedule.</p>
            <p class="loop-step"><b>Response:</b> Train at home, or choose a gym that is close to the house or your work place.</p>
            <p class="loop-step"><b>Reward:</b> Log the workout in your journal or calendar. Progress makes you feel good, it’s a reward.</p>
            <div class="contribute"><svg viewBox="0 0 16 16"><path d="M1 12.5V15h2.5l8.4-8.4-2.5-2.5zM14.8 3.7a.7.7 0 0 0 0-1L13.3 1.2a.7.7 0 0 0-1 0l-1.2 1.2 2.5 2.5z"/></svg>Contribute</div>
            <p class="section-label">Author</p>
            <div class="author"><span class="avatar-sm" role="img" aria-label="Author photo" style="background:linear-gradient(135deg,#e4d9cf,#9a8d83)"></span>Marla Quinby</div>
          </article>
          <article class="card placeholder"></article>
        </div>
        <div class="feed-col offset">
          <article class="card">
            <span class="tag bad">Bad</span>
            <svg class="like" viewBox="0 0 20 20"><path d="M10 18 2.6 10.6A4.6 4.6 0 0 1 10 4.4a4.6 4.6 0 0 1 7.4 6.2z" fill="#9d9d9d"/></svg>
            <p class="section-label">Habit</p>
            <h2 class="habit-title">Excessive Snacking</h2>
            <p class="section-label">Loop</p>
            <p class="loop-step"><b>Cue:</b> Get rid of all snacks in your house or apartment. Out of sight out of mind. This may not be possible, but that’s the idea.</p>
            <p class="loop-step"><b>Craving:</b> 99% of these snacks have little nutritional value and they belong in the garbage, not your stomach.</p>
            <p class="loop-step"><b>Response:</b> On your way to work, take a different route so you don’t pass the convenience store every time.</p>
            <p class="loop-step"><b>Reward:</b> Every time you eat an unhealthy snack, you must log it in a journal.</p>
            <div class="contribute"><svg viewBox="0 0 16 16"><path d="M1 12.5V15h2.5l8.4-8.4-2.5-2.5zM14.8 3.7a.7.7 0 0 0 0-1L13.3 1.2a.7.7 0 0 0-1 0l-1.2 1.2 2.5 2.5z"/></svg>Contribute</div>
            <p class="section-label">Author</p>
            <div class="author"><span class="avatar-sm" role="img" aria-label="Author photo" style="background:linear-gradient(135deg,#6c6a68,#2f2c2a)"></span>Dorian Vell</div>
          </article>
        </div>
      </div>
    </main>
  </div>
</div>
</body>
</html>
```